Design for Viral Content Website

In need of a webdesign for a website with mostly viral stories. There are three versions of a landingpage:
a) Whole article on one page
b) Article split into several pages each with image and previous/next buttons
c) Mobile version
I uploaded very rough versions of how it should look like. Don't judge me, if I would be a designer, I'd do it myself ;)
Don't have a mockup for the index/category listing, surprise me :)
The header must be small (as here on quirkpanel) because it will be fixed and scroll when the user scrolls down.
Number of Pages Required
4 page

```html
<!DOCTYPE html>
<html lang="en">
<head>
<meta charset="utf-8">
<title>Viral Content</title>
<link rel="stylesheet" href="https://fonts.googleapis.com/css2?family=Open+Sans:wght@400;600;700&family=Tinos&display=swap">
<style>
:root{
  --pink:#e33d8f;
  --pink-soft:#f3a6cb;
  --ink:#333333;
  --muted:#777777;
  --line:#e6e6e6;
  --page:#f1f0f0;
  --card:#ffffff;
  --footer:#2c2c2c;
  --row:#ececec;
}
*{box-sizing:border-box;margin:0;padding:0}
html,body{width:1200px;height:3805px;overflow:hidden}
body{position:relative;background:var(--page);font-family:"Open Sans",Arial,sans-serif;color:var(--ink)}
.top-band{position:absolute;left:0;top:0;width:1200px;height:8px;background:var(--pink)}
.site-header{position:absolute;left:0;top:8px;width:1200px;height:175px;background:var(--card);border-bottom:1px solid var(--line)}
.logo{position:absolute;left:0;top:28px;width:1200px;text-align:center;font-family:"Tinos",serif;font-size:34px;line-height:36px;color:#111;letter-spacing:1px}
.main-nav{position:absolute;left:0;top:132px;width:1200px;height:43px;border-top:1px solid var(--line)}
.main-nav a{position:absolute;top:12px;font-size:13px;color:var(--ink);text-decoration:none;letter-spacing:.3px}
.main-nav a.active{color:var(--pink)}
.search{position:absolute;left:1098px;top:3px;width:36px;height:36px;border-radius:50%;background:var(--pink)}
.card{position:absolute;background:var(--card);border:1px solid #e4e4e4}
.post{left:56px;width:728px;height:817px}
.post-date{position:absolute;top:22px;width:100%;text-align:center;font-size:13px;color:var(--muted)}
.post-title{position:absolute;top:52px;width:100%;text-align:center;font-size:23px;font-weight:600;letter-spacing:1px;color:#222}
.post-meta{position:absolute;top:94px;width:100%;text-align:center;font-size:12px;color:var(--ink)}
.post-meta span{margin:0 14px}
.post-meta em{font-style:normal;color:#aaa}
.post-media{position:absolute;left:0;top:137px;width:726px;height:432px}
.post-excerpt{position:absolute;left:24px;top:592px;width:680px;font-size:14px;line-height:30px;color:#555}
.post-rule{position:absolute;left:24px;right:24px;top:698px;border-top:1px solid var(--line)}
.read-more{position:absolute;left:24px;top:741px;width:111px;height:41px;background:var(--pink);color:#fff;font-size:12px;line-height:41px;text-align:center;letter-spacing:.5px}
.share{position:absolute;right:22px;top:749px;width:28px;height:28px;border-radius:50%;background:var(--pink)}
.share-row{position:absolute;right:22px;top:749px;display:flex;gap:13px}
.share-row i{width:28px;height:28px;border-radius:50%;background:#1e1e1e;display:block}
.share-row i.accent{background:var(--pink)}
.slide-arrow{position:absolute;top:330px;width:44px;height:58px;background:#fff}
.slide-arrow.prev{left:0}
.slide-arrow.next{right:0}
.video-bar{position:absolute;left:45px;top:362px;width:642px;height:34px;background:rgba(20,20,20,.85)}
.video-bar .play{position:absolute;left:0;top:0;width:50px;height:34px;background:#111}
.video-bar .track{position:absolute;left:64px;top:15px;width:470px;height:5px;background:#666}
.video-bar .track b{display:block;width:180px;height:5px;background:var(--pink)}
.side{left:817px;width:322px}
.widget-title{position:absolute;left:20px;top:16px;font-size:13px;font-weight:700;letter-spacing:.8px;color:#222}
.widget-title::after{content:"";display:block;width:282px;height:2px;margin-top:6px;background:linear-gradient(90deg,var(--pink) 35%,var(--line) 35%)}
.about-photo{position:absolute;left:20px;top:58px;width:284px;height:182px;background:linear-gradient(135deg,#d8b58c,#b98a62 55%,#e9d6c2)}
.about-name{position:absolute;left:20px;top:256px;font-size:14px;font-weight:700;letter-spacing:.5px}
.about-text{position:absolute;left:20px;top:285px;width:284px;font-size:12px;line-height:20px;color:#555}
.about-social{position:absolute;left:20px;top:362px;display:flex;gap:10px}
.about-social i{width:35px;height:35px;border:1px solid #ddd;background:#f7f7f7;display:block}
.feed{position:absolute;left:20px;width:284px;height:98px}
.feed-thumb{position:absolute;left:0;top:0;width:112px;height:92px}
.feed-title{position:absolute;left:122px;top:2px;font-size:12px;color:var(--pink);letter-spacing:.3px}
.feed-text{position:absolute;left:122px;top:22px;width:162px;font-size:11px;line-height:17px;color:#555}
.feed-date{position:absolute;left:0;top:104px;font-size:11px;color:#444}
.follow-row{position:absolute;left:20px;width:284px;height:36px;background:var(--row)}
.follow-row i{position:absolute;left:0;top:0;width:36px;height:36px;display:block}
.follow-row span{position:absolute;left:52px;top:10px;font-size:11px;color:#666}
.ad{left:817px;width:322px;border:none;overflow:hidden}
.ad-photo{position:absolute;left:0;top:0;width:322px}
.ad-name{position:absolute;left:0;width:322px;text-align:center;font-size:32px;font-weight:700;color:#7a1f2b}
.ad-price{position:absolute;left:0;width:322px;text-align:center;font-size:30px;font-weight:700;color:#c4213a}
.ad-cta{position:absolute;left:99px;width:124px;height:34px;background:#3a0e12;color:#fff;font-size:15px;font-weight:700;text-align:center;line-height:34px}
.pagination{position:absolute;left:56px;top:3670px;display:flex;gap:10px}
.pagination span{width:33px;height:38px;background:#fff;border:1px solid #e2e2e2;font-size:13px;text-align:center;line-height:36px}
.foot-line{position:absolute;left:0;top:3748px;width:1200px;height:7px;background:var(--pink)}
.site-footer{position:absolute;left:0;top:3755px;width:1200px;height:50px;background:var(--footer);font-size:12px;color:#aaa}
.foot-links{position:absolute;left:54px;top:16px}
.foot-links a{color:#bbb;text-decoration:none}
.foot-links a.active{color:var(--pink)}
.foot-links b{font-weight:400;margin:0 8px;color:#777}
.copyright{position:absolute;right:56px;top:16px}
</style>
</head>
<body>
<div class="top-band"></div>
<header class="site-header">
  <div class="logo">VIRAL<br>CONTENT</div>
  <nav class="main-nav">
    <a class="active" style="left:54px">HOME</a>
    <a style="left:168px">ABOUT US</a>
    <a style="left:314px">CATEGORIES</a>
    <a style="left:471px">VIRAL STORIES</a>
    <a style="left:640px">CREATE NEW ACCOUNT</a>
    <a style="left:870px">CONTACT</a>
    <span class="search"><svg width="36" height="36" viewBox="0 0 36 36"><circle cx="16" cy="16" r="6" fill="none" stroke="#fff" stroke-width="2"/><line x1="20.5" y1="20.5" x2="25" y2="25" stroke="#fff" stroke-width="2.4" stroke-linecap="round"/></svg></span>
  </nav>
</header>

<!-- Posts -->
<article class="card post" style="top:228px">
  <div class="post-date">SATAURDAY, DECEMBER 06, 2015</div>
  <h2 class="post-title">LOREM ISPUM DOLAR SIT AMET</h2>
  <div class="post-meta"><span><em>Posted by</em> AMET LORAM</span><span>VIRAL FEATUREDS</span><span>10 COMMENTS</span></div>
  <div class="post-media" role="img" aria-label="Couple sitting together on a dark leather sofa" style="background:linear-gradient(120deg,#2a2623,#5a4a3e 45%,#8a96a6 75%,#3b3a3c)"></div>
  <div class="slide-arrow prev" style="top:330px"><svg width="44" height="58"><polyline points="26,20 17,29 26,38" fill="none" stroke="#333" stroke-width="2"/></svg></div>
  <div class="slide-arrow next" style="top:330px"><svg width="44" height="58"><polyline points="18,20 27,29 18,38" fill="none" stroke="#333" stroke-width="2"/></svg></div>
  <p class="post-excerpt">Lorem ipsum dolor sit amet, consectetur adipiscing elit aenean non dui turpis. Nulla ullamcorper dapibu ex nec faucibus. Nunc sed fringilla velit. Vestibulum tempor ex eget cursus luctus. Phasellus ex lacus ultricie a nibh eget, accumsan hendrerit justo. Phasellus metus libero, maximus a eros sit amet, convallis hendrerit</p>
  <div class="post-rule"></div>
  <div class="read-more">READ MORE</div>
  <div class="share-row"><i></i><i></i><i></i><i></i><i></i><i></i><i class="accent"></i></div>
</article>

<article class="card post" style="top:1086px">
  <div class="post-date">SUNDAY, DECEMBER 07, 2015</div>
  <h2 class="post-title">LOREM ISPUM DOLAR SIT AMET</h2>
  <div class="post-meta"><span><em>Posted by</em> SAMET LORAM</span><span>VIRAL EATUREDS</span><span>10 COMMENTS</span></div>
  <div class="post-media" role="img" aria-label="Video still of friends running along a beach" style="background:linear-gradient(180deg,#9fb3c4,#c4cdd2 40%,#8a8a86 65%,#b7aa96)"></div>
  <div class="video-bar" style="top:499px">
    <div class="play"><svg width="50" height="34"><polygon points="20,10 31,17 20,24" fill="#fff"/></svg></div>
    <div class="track"><b></b></div>
  </div>
  <p class="post-excerpt">Lorem ipsum dolor sit amet, consectetur adipiscing elit aenean non dui turpis. Nulla ullamcorper dapibu ex nec faucibus. Nunc sed fringilla velit. Vestibulum tempor ex eget cursus luctus. Phasellus ex lacus ultricie a nibh eget, accumsan hendrerit justo. Phasellus metus libero, maximus a eros sit amet, convallis hendrerit</p>
  <div class="post-rule"></div>
  <div class="read-more">READ MORE</div>
  <div class="share"></div>
</article>

<article class="card post" style="top:1948px">
  <div class="post-date">MONDAY, DECEMBER 14, 2015</div>
  <h2 class="post-title">LOREM ISPUM DOLAR SIT AMET</h2>
  <div class="post-meta"><span><em>Posted by</em> RINA LORAM</span><span>VIRAL EATUREDS</span><span>10 COMMENTS</span></div>
  <div class="post-media" role="img" aria-label="Busy city square with yellow taxis and billboards" style="background:linear-gradient(180deg,#6f8fb6,#8a6f68 40%,#5a5552 70%,#c9a63a 85%,#555)"></div>
  <div class="slide-arrow prev"><svg width="44" height="58"><polyline points="26,20 17,29 26,38" fill="none" stroke="#333" stroke-width="2"/></svg></div>
  <div class="slide-arrow next"><svg width="44" height="58"><polyline points="18,20 27,29 18,38" fill="none" stroke="#333" stroke-width="2"/></svg></div>
  <p class="post-excerpt">Lorem ipsum dolor sit amet, consectetur adipiscing elit aenean non dui turpis. Nulla ullamcorper dapibu ex nec faucibus. Nunc sed fringilla velit. Vestibulum tempor ex eget cursus luctus. Phasellus ex lacus ultricie a nibh eget, accumsan hendrerit justo. Phasellus metus libero, maximus a eros sit amet, convallis hendrerit</p>
  <div class="post-rule"></div>
  <div class="read-more">READ MORE</div>
  <div class="share"></div>
</article>

<article class="card post" style="top:2808px">
  <div class="post-date">WEDNESDAY, DECEMBER 13, 2015</div>
  <h2 class="post-title">LOREM ISPUM DOLAR SIT AMET</h2>
  <div class="post-meta"><span><em>Posted by</em> AMET LORAM</span><span>VIRAL FEATUREDS</span><span>10 COMMENTS</span></div>
  <div class="post-media" role="img" aria-label="Woman in a sun hat sitting on a wooden deck beside a bicycle" style="background:linear-gradient(135deg,#d9c9a0,#9c8a66 40%,#6b5a44 70%,#c8b596)"></div>
  <p class="post-excerpt">Lorem ipsum dolor sit amet, consectetur adipiscing elit aenean non dui turpis. Nulla ullamcorper dapibu ex nec faucibus. Nunc sed fringilla velit. Vestibulum tempor ex eget cursus luctus. Phasellus ex lacus ultricie a nibh eget, accumsan hendrerit justo. Phasellus metus libero, maximus a eros sit amet, convallis hendrerit</p>
  <div class="post-rule"></div>
  <div class="read-more">READ MORE</div>
  <div class="share"></div>
</article>

<!-- Sidebar -->
<aside class="card side" style="top:228px;height:414px">
  <div class="widget-title">ABOUT</div>
  <div class="about-photo" role="img" aria-label="Portrait of the blog author"></div>
  <div class="about-name">LOREM ISPUM DOLAR</div>
  <p class="about-text">Write a short description about your self and what you do. That way your blog readers could get to know you better.</p>
  <div class="about-social"><i></i><i></i><i></i><i></i><i></i></div>
</aside>

<aside class="card side" style="top:685px;height:507px">
  <div class="widget-title">TWITER FEEDS</div>
  <div class="feed" style="top:56px"><div class="feed-thumb" role="img" aria-label="Feed thumbnail photo" style="background:linear-gradient(135deg,#e8d2c0,#b98f76)"></div><div class="feed-title">BUTTERFLY FLY SKY</div><div class="feed-text">Eodem modopinu nsiden turarumd dolor arfiant...</div><div class="feed-date">1 DEC 2015</div></div>
  <div class="feed" style="top:167px"><div class="feed-thumb" role="img" aria-label="Feed thumbnail photo" style="background:linear-gradient(135deg,#c9d3de,#8d8f96)"></div><div class="feed-title">WOMEN AND GIRLS</div><div class="feed-text">Eodem modopinu nsiden turarumd dolor arfiant...</div><div class="feed-date">5 DEC2015</div></div>
  <div class="feed" style="top:266px"><div class="feed-thumb" role="img" aria-label="Feed thumbnail photo" style="background:linear-gradient(135deg,#f2e4d6,#c9a487)"></div><div class="feed-title">LOREM ISPUM DOALR</div><div class="feed-text">Eodem modopinu nsiden turarumd dolor arfiant...</div><div class="feed-date">8 DEC 2015</div></div>
  <div class="feed" style="top:381px"><div class="feed-thumb" role="img" aria-label="Feed thumbnail photo" style="background:linear-gradient(135deg,#4d8fb8,#b0665a)"></div><div class="feed-title">LOREM ISPUM DOALR</div><div class="feed-text">Eodem modopinu nsiden turarumd dolor arfiant...</div><div class="feed-date">10 DEC 2015</div></div>
</aside>

<aside class="card side" style="top:1233px;height:332px">
  <div class="widget-title">FOLLOW US</div>
  <div class="follow-row" style="top:58px"><i style="background:#55acee"></i><span>533 Followers</span></div>
  <div class="follow-row" style="top:101px"><i style="background:#3b5998"></i><span>3449 Likes</span></div>
  <div class="follow-row" style="top:144px"><i style="background:#d9302b"></i><span>1943 Subscribes</span></div>
  <div class="follow-row" style="top:187px"><i style="background:#dd4b39"></i><span>3449 followers</span></div>
  <div class="follow-row" style="top:231px"><i style="background:#cb2027"></i><span>16533 Followers</span></div>
  <div class="follow-row" style="top:274px"><i style="background:#517fa4"></i><span>78564 followers</span></div>
</aside>

<div class="card ad" style="top:1601px;height:649px;background:#f4ece4">
  <div class="ad-photo" role="img" aria-label="Model in a navy embroidered gown" style="height:520px;background:linear-gradient(180deg,#efe4d8,#3a3f5c 40%,#1f2340 75%,#e8ddd2)"></div>
  <div class="ad-name" style="top:522px">Loomhaven.com</div>
  <div class="ad-price" style="top:566px">₹ 1,699</div>
  <div class="ad-cta" style="top:608px">SHOP NOW</div>
</div>

<div class="card ad" style="top:2286px;height:619px;background:#f6efe8">
  <div class="ad-photo" role="img" aria-label="Model in a yellow gown with blue embroidery" style="height:480px;background:linear-gradient(180deg,#efe6dc,#3d4fa8 30%,#f0e14a 55%,#f5ea6a 90%)"></div>
  <div class="ad-name" style="top:484px">Loomhaven.com</div>
  <div class="ad-price" style="top:528px">₹ 1,499</div>
  <div class="ad-cta" style="top:572px">SHOP NOW</div>
</div>

<div class="pagination"><span>1</span><span>2</span><span>3</span><span>»</span></div>

<div class="foot-line"></div>
<footer class="site-footer">
  <div class="foot-links"><a class="active">Home</a><b>/</b><a>about us</a><b>/</b><a>Categories</a><b>/</b><a>Viral Stories</a><b>/</b><a>Create Your Account</a><b>/</b><a>Contact</a></div>
  <div class="copyright">Copyright 2016 viral Content. All rights reserved.</div>
</footer>
</body>
</html>
```